Website for SaaS CRM software

We require a cool website for a new SaaS CRM software. The design needs to be slick and modern. I quite like the look of sites like PostOtter.

The character 'Marla' in the video is the main character which we would like to incorporate on each page if possible. Like the chimp on Postotter website.

'Sign Up Free' button or form to feature throughout the site so we have a strong call to action.

Here is a short video which will give you an idea of the software:
https://clipvault.example/83920417
Password: trelbq

You can login to the user software (backend) for screen grabs and to see what the software is all about:
www.taskloomhq.example
Username: tenant7
Password: tenant7

Please note: The website is for the front end which is where we sell the software and NOT once the user has logged in.

Target Market(s)

Small businesses, freelancers, designers, 1-man businesses

Industry/Entity Type

Software

Requirements
Must have
• 1. Opt-in box for getting started for free:

'Sign up for your Free account'

2. Logos for social media : Fb/Twitter/YouTube/LinkedIn / G+
3. Facebook 'LIKE' button
4.The Navigation Bar should always be on display at the top when scrolling
5. Login button near the Navigation Bar
6. Login page or pop-up should also have 'Forgot Password' link which prompts them to enter their email so a password can be emailed to them.

5 pages & a blog in total. The pages we require are:

HOME
- Heading 'Easy to use small business software'
- Should have a video placeholder and some bullet points or tick marks for key features. The video (from YouTube) should open up on a bigger lightbox and the background greyed out.
- Sign up box to have the fields for First Name, Company Name, Email & Password with a check box for 'I agree with Terms & Conditions'

TOUR
Sub-Navigation bar at the top or side bar with the headings for each module i.e CONTACTS, QUOTES, JOBS, DIARY, SALES, PURCHASES, PRODUCTS, REPORTS
Each module with need to have a placeholder for an image or video and 1 paragraph of text explaining key features. Please see http://postotter.example/features/

See how the Navigation buttons stay visible at all times and changes to the next button when scrolling: http://postotter.example/features/

No side bar on this page.

PRICING
Pricing table of 3 to 4 columns with a button at the bottom. This software is a monthly subscription, so we need to show the $/month for each Plan at the top with the name of the Plan
The plans are:
Bronze: Free
Silver: $20/month
Gold: $40 / month
Platinum: $75 / month

No side bar on this page.

Heading at the bottom: 'No minimum contract. Cancel anytime.'

SUPPORT PAGE
This to a contact form to submit a ticket for tech support. We also need a 2-column list for videos which we will put up. The video open up on a lightbox in bigger size.

No side bar on this page.

CONTACT
Contact details i.e name, address, telephone, email & a contact form
No side bar on this page.

BLOG
Pagecraft blog. I love the way the headings, paragraph, font, line spacing, colours are on the PostOtter blog.

Need a side bar.

```html
<!DOCTYPE html>
<html lang="en">
<head>
<meta charset="utf-8">
<title>Taskloom – Our Plan Pricing</title>
<link rel="stylesheet" href="https://fonts.googleapis.com/css2?family=Questrial&family=Alegreya+Sans:ital,wght@1,400&family=Arimo&family=Nothing+You+Could+Do&family=Montserrat:wght@700&display=swap">
<style>
  :root{
    --page-cream:#fcfcdc;
    --brand-blue:#03a9f4;
    --nav-blue:#1797d6;
    --ink:#222;
    --text:#444;
    --muted:#888;
    --rule:#e6e6e6;
    --head-band:#eeeeee;
    --col-bg:#f8f8fa;
    --price-bg:#fbfaf7;
  }
  *{box-sizing:border-box;margin:0;padding:0}
  html,body{width:1200px;height:1192px;overflow:hidden}
  body{background:var(--page-cream);position:relative;font-family:"Arimo",sans-serif;color:var(--text)}

  .site-header{position:absolute;left:0;top:0;width:1200px;height:76px;border-bottom:2px solid var(--brand-blue)}
  .brand{position:absolute;left:68px;top:8px;display:flex;align-items:center;gap:12px;
    font-family:"Montserrat",sans-serif;font-weight:700;font-size:52px;color:var(--ink);letter-spacing:-1px;line-height:60px}
  .brand-dot{width:22px;height:22px;border-radius:50%;background:var(--brand-blue)}
  .main-nav{position:absolute;top:30px;left:0;width:1200px;height:30px}
  .main-nav a{position:absolute;font-family:"Questrial",sans-serif;font-size:21px;color:var(--nav-blue);
    text-decoration:none;text-transform:uppercase;letter-spacing:-.5px;line-height:30px;white-space:nowrap}
  .nav-marker{position:absolute;left:845px;top:64px;width:0;height:0;
    border-left:10px solid transparent;border-right:10px solid transparent;border-bottom:10px solid var(--brand-blue)}
  .login-btn{position:absolute;left:1118px;top:5px;width:70px;height:22px;background:var(--brand-blue);
    border-radius:3px;font-family:"Questrial",sans-serif;font-size:12px;color:#fff;line-height:22px;
    text-align:center;text-transform:uppercase;text-decoration:none}

  .page-title-bar{position:absolute;left:0;top:76px;width:1200px;height:66px;
    background:linear-gradient(#fff,#f4f4f4);border-bottom:1px solid var(--rule)}
  .page-title{position:absolute;left:45px;top:17px;font-family:"Questrial",sans-serif;font-size:25px;color:#3d3d3d;font-weight:400}
  .breadcrumb{position:absolute;left:939px;top:24px;font-family:"Questrial",sans-serif;font-size:15px;color:#333;text-transform:uppercase}
  .breadcrumb a{color:var(--brand-blue);text-decoration:none}
  .breadcrumb span{margin:0 6px}

  .content{position:absolute;left:0;top:142px;width:1200px;height:682px;background:#fff}

  .pricing-wrap{position:absolute;left:48px;top:54px;width:1071px;height:558px;background:#f5f5f5}
  .pricing-table{position:absolute;left:11px;top:13px;width:1049px;height:533px;border:1px solid #d9d9d9;border-radius:3px;background:var(--col-bg)}
  .plan{position:absolute;top:0;height:531px;text-align:center}
  .plan-bronze{left:0;width:241px}
  .plan-silver{left:564px;width:241px}
  .plan-platinum{left:805px;width:242px;border-left:1px solid #e2e2e2}
  .plan-name{height:53px;background:var(--head-band);font-family:"Questrial",sans-serif;font-size:22px;color:var(--ink);
    line-height:56px;text-transform:uppercase}
  .plan-price{position:absolute;left:0;right:0;top:70px;height:50px;background:var(--price-bg);
    border-top:1px solid #eee;border-bottom:1px solid #eee;font-family:"Alegreya Sans",sans-serif;font-style:italic;
    font-size:21px;color:#333;line-height:48px}
  .plan-term{position:absolute;left:0;right:0;top:134px;font-family:"Questrial",sans-serif;font-size:14px;color:#444;text-transform:uppercase}
  .plan-features{position:absolute;left:18px;right:18px;top:168px;list-style:none}
  .plan-features li{height:68px;border-top:1px solid var(--rule);padding-top:12px;font-size:15px;line-height:25px;color:#333}
  .plan-features li small{display:block;font-size:15px;color:var(--muted)}
  .select-btn{position:absolute;left:50%;top:404px;transform:translateX(-50%);width:137px;height:69px;
    background:var(--brand-blue);border:1px solid #111;border-radius:3px;box-shadow:0 2px 3px rgba(0,0,0,.35);
    font-family:"Questrial",sans-serif;font-size:29px;color:#fff;line-height:66px;text-transform:uppercase}

  .plan-featured{position:absolute;left:242px;top:-23px;width:322px;height:559px;background:#fff;border-radius:4px;
    box-shadow:0 0 8px rgba(0,0,0,.25);text-align:center}
  .plan-featured .panel{position:absolute;left:5px;top:5px;width:312px;height:536px;background:var(--price-bg)}
  .plan-featured .plan-name{height:70px;font-size:30px;line-height:66px;background:var(--head-band)}
  .plan-featured .plan-price{top:88px;color:var(--brand-blue);font-size:28px}
  .plan-featured .plan-term{top:152px}
  .plan-featured .plan-features{top:186px}
  .plan-featured .select-btn{top:430px;width:184px}

  .contract-note{position:absolute;left:0;width:1200px;top:636px;text-align:center;
    font-family:"Questrial",sans-serif;font-size:22px;font-weight:400;color:#3d3d3d}

  .testimonial-band{position:absolute;left:0;top:824px;width:1200px;height:78px;
    background:linear-gradient(#151515,#2a2a2a 40%,#1a1a1a);border-bottom:4px solid #0d0d0d}
  .testimonial{position:absolute;left:68px;top:24px;font-family:"Nothing You Could Do",cursive;font-size:19px;color:#666}
</style>
</head>
<body>
  <header class="site-header">
    <div class="brand"><span>taskloom</span><span class="brand-dot"></span></div>
    <a href="#" class="login-btn">Login</a>
    <nav class="main-nav">
      <a href="#" style="left:668px">Home</a>
      <a href="#" style="left:748px">Tour</a>
      <a href="#" style="left:820px">Pricing</a>
      <a href="#" style="left:918px">Support</a>
      <a href="#" style="left:1025px">Contact</a>
      <a href="#" style="left:1140px">Blog</a>
    </nav>
    <div class="nav-marker"></div>
  </header>

  <div class="page-title-bar">
    <h1 class="page-title">OUR PLAN PRICING</h1>
    <div class="breadcrumb"><a href="#">Home</a><span>/</span>Our Plan Pricing</div>
  </div>

  <main class="content">
    <div class="pricing-wrap">
      <div class="pricing-table">
        <div class="plan plan-bronze">
          <div class="plan-name">Bronze</div>
          <div class="plan-price">$0.00</div>
          <div class="plan-term">Unlimited Trial Offer</div>
          <ul class="plan-features">
            <li>Instant Setup<small>Immediate activation</small></li>
            <li>24/7 Support<small>Online support</small></li>
            <li>No Term Contract<small>Cancel anytime</small></li>
          </ul>
          <div class="select-btn">Select</div>
        </div>

        <div class="plan-featured">
          <div class="panel">
            <div class="plan-name">Gold</div>
            <div class="plan-price">$40.00</div>
            <div class="plan-term">Per Month</div>
            <ul class="plan-features">
              <li>Instant Setup<small>Immediate account provisioning</small></li>
              <li>24/7 Support<small>Live on demand support</small></li>
              <li>No Term Contract<small>Cancel Anytime</small></li>
            </ul>
            <div class="select-btn">Select</div>
          </div>
        </div>

        <div class="plan plan-silver">
          <div class="plan-name">Silver</div>
          <div class="plan-price">$20.00</div>
          <div class="plan-term">Per Month</div>
          <ul class="plan-features">
            <li>Instant Setup<small>Immediate activation</small></li>
            <li>24/7 Support<small>Online support</small></li>
            <li>No Term Contract<small>Cancel Anytime</small></li>
          </ul>
          <div class="select-btn">Select</div>
        </div>

        <div class="plan plan-platinum">
          <div class="plan-name">Platinum</div>
          <div class="plan-price">$75.00</div>
          <div class="plan-term">Per Month</div>
          <ul class="plan-features">
            <li>Instant Setup<small>Immediate activation</small></li>
            <li>24/7 Support<small>On demand support</small></li>
            <li>No Term Contract<small>Cancel Anytime</small></li>
          </ul>
          <div class="select-btn">Select</div>
        </div>
      </div>
    </div>
    <h2 class="contract-note">No minimum contract. Cancel anytime.</h2>
  </main>

  <section class="testimonial-band">
    <p class="testimonial">"One word - Terrific! I am a definitely life-long happy customer." Jon Pell, Ridgeway Co.</p>
  </section>
</body>
</html>
```